redesign existing business card

Re design our business cards. We want a modern elegant design, open to ideas front side must contain similar details in a fresh look and style, back side we are open to suggestions. MUST USE COMPANY COLORS, WE WANT BRANDING. Need more ideas see www.brightstoneyards.com - Project must be done in one of adobe products and all files and fonts must be submitted to us. THIS IS A MUST

Target Market(s)

home owners

Industry/Entity Type

Construction Company

Contact Information for Business Card

see existing card file for information

Font styles to use
Sans Serif

Colors
0455a3
3377b5
34a6d7
0592cd
85cae6
ffffff

Requirements
Must have
• company colors, logo, contact info this is all for front side. back side be creative.

```html
<!DOCTYPE html>
<html lang="en">
<head>
<meta charset="utf-8">
<title>Brightstone Yards – Business Cards</title>
<link href="https://fonts.googleapis.com/css2?family=PT+Serif:wght@400;700&family=Roboto+Slab:wght@700&display=swap" rel="stylesheet">
<style>
  :root{
    --brand-deep:#0455a3;
    --brand-mid:#3377b5;
    --brand-sky:#34a6d7;
    --brand-bright:#0592cd;
    --brand-pale:#85cae6;
    --white:#ffffff;
    --ink:#1d1d1f;
    --navy:#0b1f3a;
    --stone-light:#f4f4f2;
    --stone-shade:#dcdcd8;
    --backdrop:#e9ebee;
  }
  *{box-sizing:border-box;margin:0;padding:0}
  html,body{width:1200px;height:1000px;overflow:hidden}
  body{background:var(--backdrop);position:relative;font-family:"PT Serif",serif}

  .card{position:absolute;width:620px;height:354px;overflow:hidden;
        box-shadow:0 6px 18px rgba(0,0,0,.18);background:var(--white)}

  /* ---------- services side ---------- */
  .card--services{left:70px;top:90px}
  .stone-wall{position:absolute;inset:0;
    background:radial-gradient(ellipse at 45% 40%,var(--stone-light) 0%,#ececea 60%,var(--stone-shade) 100%)}
  .services-brand{position:absolute;left:40px;top:150px;width:250px;
    display:flex;align-items:center;gap:12px}
  .brand-mark{width:22px;height:22px;background:var(--brand-deep);flex:none}
  .brand-name{font-family:"PT Serif",serif;font-weight:700;font-size:30px;line-height:1.05;
    color:var(--brand-deep);text-transform:uppercase;letter-spacing:.5px}
  .service-list{position:absolute;right:40px;top:30px;width:290px;list-style:none;text-align:center;
    font-family:"Roboto Slab",serif;font-weight:700;font-size:17px;line-height:23px;color:var(--ink);
    text-transform:uppercase;letter-spacing:.3px}
  .family-note{position:absolute;right:40px;top:208px;width:290px;text-align:center;
    font-family:"PT Serif",serif;font-size:17px;color:var(--brand-bright);text-transform:uppercase}
  .licence{position:absolute;right:40px;top:240px;width:290px;text-align:right;
    font-size:13px;line-height:19px;color:#333;text-transform:uppercase}
  .licence .lead{text-transform:none}

  /* ---------- contact side ---------- */
  .card--contact{left:510px;top:560px}
  .contact-sweep{position:absolute;inset:0}
  .contact-info{position:absolute;left:34px;top:30px;color:var(--white);font-size:17px;line-height:23px}
  .person-name{font-size:27px;letter-spacing:1.5px;text-transform:uppercase;margin-bottom:16px;font-weight:400}
  .contact-group{margin-bottom:18px}
  .group-label{color:var(--navy);text-transform:uppercase;letter-spacing:.5px}
  .contact-brand{position:absolute;right:34px;top:118px;width:220px;
    display:flex;align-items:center;gap:10px;justify-content:flex-end}
  .contact-brand .brand-name{font-size:24px;text-align:left}
  .website{position:absolute;right:34px;top:232px;font-size:18px;color:var(--brand-bright)}
</style>
</head>
<body>

<section class="card card--services" aria-label="Services side">
  <div class="stone-wall" role="img" aria-label="White painted brick wall texture"></div>
  <div class="services-brand">
    <span class="brand-mark"></span>
    <span class="brand-name">Brightstone<br>Yards</span>
  </div>
  <ul class="service-list">
    <li>Driveway</li>
    <li>Pool Renovation</li>
    <li>Custom Out-Door Kitchen</li>
    <li>Retaining Wall</li>
    <li>Paver Restoration</li>
    <li>H.O.A Projects</li>
    <li>Patios &amp; Much More</li>
  </ul>
  <p class="family-note">Family Owned &amp; Operated</p>
  <p class="licence">
    <span class="lead">Licence &amp; Insured</span><br>
    CTY 24-HS-30417-R SHR U-58210<br>
    County HSC7319
  </p>
</section>

<section class="card card--contact" aria-label="Contact side">
  <svg class="contact-sweep" width="620" height="354" viewBox="0 0 620 354" aria-hidden="true">
    <path d="M0 0 H486 C380 70 380 280 282 354 H0 Z" fill="var(--brand-pale)"/>
    <path d="M0 0 H474 C368 70 368 280 270 354 H0 Z" fill="var(--brand-bright)"/>
  </svg>
  <div class="contact-info">
    <h1 class="person-name">Marco Lindqvist</h1>
    <div class="contact-group">
      <p>Direct: (555) 214-3087</p>
      <p>marco@brightstoneyards.com</p>
    </div>
    <div class="contact-group">
      <p class="group-label">Office Showroom</p>
      <p>2280 Harbor View Dr Suite 6</p>
      <p>Coral Bend, FL 33999</p>
    </div>
    <div class="contact-group">
      <p>O: (555) 380-4471</p>
      <p>F: (555) 380-4472</p>
    </div>
  </div>
  <div class="contact-brand">
    <span class="brand-mark"></span>
    <span class="brand-name">Brightstone<br>Yards</span>
  </div>
  <p class="website">www.brightstoneyards.com</p>
</section>

</body>
</html>
```